Glow Up by Lakeside 21 day Challenge

We are having a Glow Up by Lakeside Challenge at our fitness studio. We need a poster design using the template attached as a reference. I have also included our Bromalux logo to put on the poster. Please DO NOT use the graphics in the flyer as we are expecting something much better :-)

-Size needed 11x17 with bleeding for printing

-We need this made in Photoshop (CS3 friendly) or at least delivered in PS as we might change some text or re-arrange the design later on.

-We need this in layers.

```html
<!DOCTYPE html>
<html lang="en">
<head>
<meta charset="utf-8">
<title>Glow Up by Lakeside 21 day Challenge – Bromalux Bootcamps</title>
<link rel="stylesheet" href="https://fonts.googleapis.com/css2?family=Rubik+Dirt&family=Arimo:wght@400;700&display=swap">
<style>
  :root {
    --paper: #ffffff;
    --navy: #061466;
    --orange: #f3922b;
    --green: #a9c23a;
    --red: #c4202f;
    --pink: #e5177e;
    --yellow: #f6d21f;
    --cream: #fbe88c;
    --teal: #3fb8b0;
    --white: #ffffff;
    --lime: #9ccb3b;
  }
  * { margin: 0; padding: 0; box-sizing: border-box; }
  html, body { width: 796px; height: 1200px; overflow: hidden; background: var(--paper); }
  .poster {
    position: relative;
    width: 796px; height: 1200px;
    background: var(--paper);
    overflow: hidden;
  }
  .panel {
    position: absolute;
    left: 35px; top: 38px; width: 726px; height: 1124px;
    background: var(--navy);
  }
  .brand {
    position: absolute;
    left: 254px; top: 94px; width: 288px; height: 94px;
    display: flex; align-items: center; justify-content: center; gap: 12px;
    border: 3px solid var(--white);
    border-radius: 6px;
  }
  .brand-mark { width: 22px; height: 22px; background: var(--white); }
  .brand-name {
    font-family: 'Arimo', Arial, sans-serif;
    font-weight: 700; font-size: 36px; color: var(--white);
    letter-spacing: 1px;
  }

  .headline { font-family: 'Rubik Dirt', 'Arial Black', sans-serif; font-weight: 400; line-height: 1; }
  .headline-line {
    position: absolute;
    display: flex; justify-content: center;
    text-transform: uppercase;
    white-space: nowrap;
    transform-origin: top center;
  }
  .headline-top {
    left: 90px; width: 620px; top: 190px;
    font-size: 140px; letter-spacing: -4px;
    transform: scaleY(1.75);
  }
  .headline-bottom {
    left: 150px; width: 600px; top: 397px;
    font-size: 116px; letter-spacing: -4px;
    transform: scaleY(1.95);
  }
  .headline-join {
    position: absolute; left: 100px; top: 470px;
    font-size: 40px; color: var(--orange);
  }
  .c-orange { color: var(--orange); }
  .c-green { color: var(--green); }
  .c-red { color: var(--red); }
  .c-pink { color: var(--pink); }
  .c-yellow { color: var(--yellow); }
  .c-cream { color: var(--cream); }
  .gap { width: 20px; }

  .pitch {
    position: absolute; left: 240px; top: 630px; width: 520px;
    font-family: 'Rubik Dirt', 'Arial Black', sans-serif;
    text-transform: uppercase; line-height: 1.17; font-size: 34px;
    white-space: nowrap;
  }
  .pitch-line { display: block; }

  .benefits {
    position: absolute; left: 240px; top: 752px; width: 410px;
    list-style: none;
    font-family: 'Arimo', Arial, sans-serif; font-weight: 700;
    font-size: 15px; line-height: 18.5px; color: var(--white);
  }
  .benefit { position: relative; padding-left: 14px; }
  .benefit::before {
    content: ""; position: absolute; left: 0; top: 7px;
    width: 7px; height: 7px; border-radius: 50%;
    background: var(--dot);
  }

  .offer {
    position: absolute; left: 240px; top: 900px; width: 520px;
    font-family: 'Rubik Dirt', 'Arial Black', sans-serif;
    text-transform: uppercase; line-height: 1.1;
    white-space: nowrap;
  }
  .offer-value { display: block; font-size: 29px; color: var(--orange); }
  .offer-price { display: block; font-size: 40px; color: var(--pink); }

  .testimonial {
    position: absolute; left: 240px; top: 986px; width: 505px;
    font-family: 'Arimo', Arial, sans-serif; font-weight: 700; color: var(--white);
  }
  .testimonial-quote { font-size: 19px; white-space: nowrap; }
  .testimonial-author { text-align: right; font-size: 13px; margin-top: 6px; font-weight: 400; }

  .urgency {
    position: absolute; left: 240px; top: 1044px;
    font-family: 'Arimo', Arial, sans-serif; font-weight: 700;
    font-size: 14px; line-height: 20px; color: var(--lime);
    text-transform: uppercase;
  }
</style>
</head>
<body>
<main class="poster">
  <div class="panel"></div>

  <div class="brand">
    <span class="brand-mark"></span>
    <span class="brand-name">Bromalux</span>
  </div>

  <h1 class="headline">
    <span class="headline-line headline-top">
      <span class="c-orange">G</span><span class="c-green">L</span><span class="c-red">O</span><span class="c-pink">W</span>
      <span class="gap"></span>
      <span class="c-yellow">U</span><span class="c-cream">P</span>
    </span>
    <span class="headline-join">by</span>
    <span class="headline-line headline-bottom">
      <span class="c-yellow">L</span><span class="c-cream">A</span><span class="c-red">K</span><span class="c-pink">E</span><span class="c-green">S</span><span class="c-orange">I</span><span class="c-yellow">D</span><span class="c-cream">E</span>
    </span>
  </h1>

  <p class="pitch">
    <span class="pitch-line c-yellow">Discover the secret to</span>
    <span class="pitch-line c-green">a beach-ready body</span>
    <span class="pitch-line c-pink">in just 21 days!</span>
  </p>

  <ul class="benefits">
    <li class="benefit" style="--dot: var(--pink)">9 total training sessions designed to incinerate fat off your midsection, thighs, and arms</li>
    <li class="benefit" style="--dot: var(--yellow)">21 days of nutritional guidance, including delicious recipes</li>
    <li class="benefit" style="--dot: var(--teal)">A Success Session to map out your individual plan for success</li>
    <li class="benefit" style="--dot: var(--red)">Your very own Personal Accountability Coach to ensure you get results</li>
  </ul>

  <p class="offer">
    <span class="offer-value">You get all this–a $399 value</span>
    <span class="offer-price">for only $99!</span>
  </p>

  <blockquote class="testimonial">
    <p class="testimonial-quote">I've never been more fit in my life—at age 41!</p>
    <p class="testimonial-author">~Marla Voss</p>
  </blockquote>

  <p class="urgency">Hurry! Space is limited to only 20 participants!!!<br>Claim your spot now</p>
</main>
</body>
</html>
```